Quorvex - Automated robotic Inspection with AI need new business cards

We need a new design of our business cards. The company is focused on automated quality control at high speed with unmatched results. We have a logo but need a more forward leaning business card that shows that we are delivering cutting edge technology.

Contact Information for Business Card

Name
Position
Adress
Phone
Email
e.g.
Lena Holmqvist
Chief Financial Officer (CFO)

Quorvex Sweden AB
Bruksvägen 14, SE-175 43 JÄRFÄLLA, Sweden
Mobile: +46735 21 47 83 | Office: +46 8 61 94 27
www.quorvex-example.com

Font styles to use
Sans Serif

```html
<!DOCTYPE html>
<html lang="en">
<head>
<meta charset="utf-8">
<title>Quorvex Business Card</title>
<link rel="stylesheet" href="https://fonts.googleapis.com/css2?family=Montserrat:wght@500;600&family=Open+Sans:wght@400;600&display=swap">
<style>
  :root {
    --brand-blue: #1c5480;
    --ink: #1d1d1b;
    --paper: #ffffff;
    --backdrop: #e9ecef;
    --back-dark: #021e33;
    --back-light: #1b5782;
  }
  * { box-sizing: border-box; margin: 0; padding: 0; }
  html, body { width: 1200px; height: 1200px; overflow: hidden; }
  body {
    background: var(--backdrop);
    font-family: "Open Sans", sans-serif;
    position: relative;
  }
  .card {
    position: absolute;
    left: 230px;
    width: 740px;
    height: 423px;
    overflow: hidden;
    box-shadow: 0 10px 30px rgba(0,0,0,0.18);
  }
  .card-front { top: 70px; background: var(--paper); }
  .card-back {
    top: 640px;
    background: linear-gradient(30deg, var(--back-dark) 25%, var(--back-light) 100%);
    color: #fff;
  }
  .wordmark {
    font-family: "Montserrat", sans-serif;
    font-weight: 600;
    letter-spacing: 2px;
    line-height: 1;
    white-space: nowrap;
  }
  .card-front .wordmark {
    position: absolute; left: 47px; top: 46px;
    font-size: 62px; color: var(--brand-blue);
  }
  .person {
    position: absolute; right: 40px; top: 162px; text-align: right;
    font-family: "Montserrat", sans-serif; line-height: 1.15;
  }
  .person-name { font-size: 27px; font-weight: 500; color: var(--brand-blue); letter-spacing: 0.5px; }
  .person-title { font-size: 22px; font-weight: 500; color: var(--ink); }
  .accent-bar {
    position: absolute; right: 0; top: 164px; width: 16px; height: 52px;
    background: var(--brand-blue);
  }
  .divider {
    position: absolute; left: 32px; top: 226px; width: 677px; height: 3px;
    background: var(--brand-blue);
  }
  .contacts { position: absolute; left: 53px; top: 250px; list-style: none; }
  .contacts li {
    display: flex; align-items: center; gap: 9px;
    font-size: 20px; color: var(--ink); height: 33px; white-space: nowrap;
  }
  .contacts li.phone { font-weight: 600; height: 40px; }
  .contacts .dot {
    width: 25px; height: 25px; border-radius: 50%;
    background: var(--brand-blue); flex: none;
  }
  .contacts .sep { margin: 0 24px 0 8px; }
  .footer-band { position: absolute; left: 0; bottom: 0; width: 740px; height: 53px; }
  .footer-url {
    position: absolute; left: 86px; bottom: 24px;
    font-size: 18px; letter-spacing: 4px; color: #fff;
    line-height: 1; white-space: nowrap;
  }
  .card-back .wordmark {
    position: absolute; left: 0; right: 0; top: 150px; text-align: center;
    font-size: 78px; color: #fff;
  }
  .back-links {
    position: absolute; left: 0; right: 0; bottom: 70px; text-align: center;
    font-size: 18px; letter-spacing: 2px; white-space: nowrap;
  }
  .back-links .sep { margin: 0 16px; }
</style>
</head>
<body>
  <section class="card card-front">
    <div class="wordmark">QUORVEX</div>
    <div class="person">
      <div class="person-name">LENA HOLMQVIST</div>
      <div class="person-title">CFO</div>
    </div>
    <div class="accent-bar"></div>
    <div class="divider"></div>
    <ul class="contacts">
      <li class="phone"><span class="dot"></span>+46735 21 47 83<span class="sep">|</span>+46 8 61 94 27</li>
      <li><span class="dot"></span>Quorvex Sweden AB, Bruksvägen 14, SE-175 43 Järfälla, Sweden</li>
      <li><span class="dot"></span>info@quorvex-example.com</li>
    </ul>
    <svg class="footer-band" viewBox="0 0 740 53" aria-hidden="true">
      <path d="M0 0 H460 Q485 0 495 14 L515 27 H740 V53 H0 Z" fill="var(--brand-blue)"/>
    </svg>
    <div class="footer-url">www.quorvex-example.com</div>
  </section>

  <section class="card card-back">
    <div class="wordmark">QUORVEX</div>
    <div class="back-links">info@quorvex-example.com<span class="sep">|</span>www.quorvex-example.com</div>
  </section>
</body>
</html>
```